Brightwell Circle OKAV: Global Policy to Local Action

We need two professional visuals that represent the vision and strategy of the organization. I attached two rough images of the first visual and one image of the second visual. I also attached a pdf of the narrative to give context for each visual.

Target Market(s)

Global Health Policy Makers

Colors
ec1f27

Requirements
Must have
• Two separate images representing the flow of the work

```html
<!DOCTYPE html>
<html lang="en">
<head>
<meta charset="utf-8">
<title>Brightwell Circle OKAV – Global Policy to Local Action</title>
<link href="https://fonts.googleapis.com/css2?family=Roboto+Condensed:wght@400;700&display=swap" rel="stylesheet">
<style>
  :root {
    --brand-red: #d4202a;
    --brand-red-light: #d23a45;
    --segment-pink: #e08a90;
    --ring-grey: #e4e4e4;
    --ring-edge: #d2d2d2;
    --map-grey: #d6d6d6;
    --ink: #3a3a3a;
    --dash: #444444;
    --accent-purple: #5a2d6c;
    --white: #ffffff;
  }
  * { margin: 0; padding: 0; box-sizing: border-box; }
  html, body { width: 1200px; height: 886px; overflow: hidden; background: var(--white); }
  body { font-family: "Roboto Condensed", "Arial Narrow", sans-serif; color: var(--ink); }
  .canvas { position: relative; width: 1200px; height: 886px; overflow: hidden; background: var(--white); }
  .header {
    position: absolute; left: 0; top: 0; width: 1200px; height: 125px;
    background: linear-gradient(90deg, var(--brand-red), var(--brand-red-light));
    display: flex; align-items: center; justify-content: center;
  }
  .header-title { color: var(--white); font-weight: 700; font-size: 33px; letter-spacing: 0.2px; }
  .diagram { position: absolute; left: 0; top: 0; }
  .info-block { position: absolute; }
  .info-heading {
    color: var(--brand-red); font-weight: 700; font-size: 14.5px; line-height: 19px;
    text-transform: uppercase; letter-spacing: 0.3px;
  }
  .info-list { list-style: none; margin-top: 9px; }
  .info-list li {
    position: relative; font-size: 14px; line-height: 19.5px; color: var(--ink);
  }
  .info-list li::before {
    content: ""; position: absolute; left: -20px; top: 4px; width: 5px; height: 9px;
    border-right: 1.6px solid var(--brand-red); border-bottom: 1.6px solid var(--brand-red);
    transform: rotate(40deg);
  }
  .frameworks { left: 97px; top: 229px; }
  .best-practices { left: 97px; top: 675px; }
  .guiding-values { left: 935px; top: 229px; }
  .outcome { left: 935px; top: 675px; }
  .axis-label {
    position: absolute; color: var(--brand-red); font-weight: 700; font-size: 14.5px;
    text-transform: uppercase; letter-spacing: 0.3px; line-height: 20px;
  }
  .axis-global { right: 976px; top: 482px; }
  .axis-local { left: 944px; top: 482px; }
  .segment-label { font-family: "Roboto Condensed", "Arial Narrow", sans-serif; font-size: 15.5px; fill: var(--white); }
  .ring-label { font-family: "Roboto Condensed", "Arial Narrow", sans-serif; font-weight: 700; font-size: 15px; fill: var(--accent-purple); }
  .hub-name { font-family: "Roboto Condensed", "Arial Narrow", sans-serif; font-size: 18px; fill: var(--ink); letter-spacing: 0.4px; }
  .hub-title { font-family: "Roboto Condensed", "Arial Narrow", sans-serif; font-size: 21px; fill: var(--ink); }
</style>
</head>
<body>
<main class="canvas">

  <svg class="diagram" width="1200" height="886" viewBox="0 0 1200 886" xmlns="http://www.w3.org/2000/svg">
    <defs>
      <radialGradient id="mapTone" cx="50%" cy="50%" r="60%">
        <stop offset="0%" stop-color="#d0d0d0"/>
        <stop offset="70%" stop-color="#dddddd"/>
        <stop offset="100%" stop-color="#ffffff" stop-opacity="0"/>
      </radialGradient>
      <path id="arcPolicy" d="M366.6 455.9 A243 243 0 0 1 481 324.4"/>
      <path id="arcPublications" d="M709 324.4 A243 243 0 0 1 823.4 455.9"/>
      <path id="arcTraining" d="M448.1 748.7 A256 256 0 0 0 741.8 748.7"/>
    </defs>

    <!-- world map area -->
    <rect class="world-map" role="img" aria-label="World map in light grey behind the diagram"
          x="90" y="190" width="1030" height="640" rx="120" fill="url(#mapTone)" opacity="0.75"/>

    <!-- dashed orbit -->
    <ellipse class="orbit" cx="595" cy="539" rx="320" ry="375" fill="none"
             stroke="var(--dash)" stroke-width="2" stroke-dasharray="7 6"/>

    <!-- outer grey ring -->
    <circle class="outer-ring" cx="595" cy="539" r="264" fill="var(--ring-grey)" stroke="var(--ring-edge)" stroke-width="1"/>

    <!-- segments -->
    <g class="segments" stroke="var(--white)" stroke-width="2">
      <path fill="var(--brand-red)" d="M522.4 315.5 A235 235 0 0 1 667.6 315.5 L640.7 398.3 A148 148 0 0 0 549.3 398.3 Z"/>
      <path fill="var(--segment-pink)" d="M667.6 315.5 A235 235 0 0 1 785.1 400.8 L714.7 452 A148 148 0 0 0 640.7 398.3 Z"/>
      <path fill="var(--brand-red)" d="M785.1 400.8 A235 235 0 0 1 830 539 L743 539 A148 148 0 0 0 714.7 452 Z"/>
      <path fill="var(--segment-pink)" d="M830 539 A235 235 0 0 1 785.1 677.2 L714.7 626 A148 148 0 0 0 743 539 Z"/>
      <path fill="var(--brand-red)" d="M785.1 677.2 A235 235 0 0 1 667.6 762.5 L640.7 679.7 A148 148 0 0 0 714.7 626 Z"/>
      <path fill="var(--segment-pink)" d="M667.6 762.5 A235 235 0 0 1 522.4 762.5 L549.3 679.7 A148 148 0 0 0 640.7 679.7 Z"/>
      <path fill="var(--brand-red)" d="M522.4 762.5 A235 235 0 0 1 404.9 677.2 L475.3 626 A148 148 0 0 0 549.3 679.7 Z"/>
      <path fill="var(--segment-pink)" d="M404.9 677.2 A235 235 0 0 1 360 539 L447 539 A148 148 0 0 0 475.3 626 Z"/>
      <path fill="var(--brand-red)" d="M360 539 A235 235 0 0 1 404.9 400.8 L475.3 452 A148 148 0 0 0 447 539 Z"/>
      <path fill="var(--segment-pink)" d="M404.9 400.8 A235 235 0 0 1 522.4 315.5 L549.3 398.3 A148 148 0 0 0 475.3 452 Z"/>
    </g>

    <!-- segment labels -->
    <g class="segment-labels" text-anchor="middle">
      <text class="segment-label" x="595" y="339">Regional</text>
      <text class="segment-label" x="595" y="359">Meetings</text>
      <text class="segment-label" x="778" y="486">Taskforces</text>
      <text class="segment-label" x="706" y="700">Conferences</text>
      <text class="segment-label" x="484" y="700">Symposiums</text>
      <text class="segment-label" x="412" y="486">Workshops</text>
    </g>

    <!-- ring labels -->
    <text class="ring-label"><textPath href="#arcPolicy" startOffset="50%" text-anchor="middle">Policy Papers</textPath></text>
    <text class="ring-label"><textPath href="#arcPublications" startOffset="50%" text-anchor="middle">Publications</textPath></text>
    <text class="ring-label"><textPath href="#arcTraining" startOffset="50%" text-anchor="middle">Training Curricula</textPath></text>

    <!-- hub -->
    <circle class="hub" cx="595" cy="539" r="146" fill="var(--white)"/>
    <text class="hub-name" x="595" y="478" text-anchor="middle">Brightwell Circle OKAV</text>
    <text class="hub-title" x="595" y="547" text-anchor="middle">Network of Networks</text>

    <!-- global policy icon -->
    <g class="icon-global">
      <circle cx="272" cy="492" r="38" fill="var(--white)" stroke="#cfcfcf" stroke-width="3"/>
      <g fill="none" stroke="var(--brand-red)" stroke-width="2">
        <circle cx="272" cy="492" r="18"/>
        <ellipse cx="272" cy="492" rx="8" ry="18"/>
        <line x1="254" y1="492" x2="290" y2="492"/>
        <path d="M257 482 H287 M257 502 H287"/>
      </g>
    </g>

    <!-- local action icon -->
    <g class="icon-local">
      <circle cx="894" cy="492" r="38" fill="var(--white)" stroke="#cfcfcf" stroke-width="3"/>
      <path d="M894 514 C884 502 879 494 879 486 A15 15 0 0 1 909 486 C909 494 904 502 894 514 Z"
            fill="none" stroke="var(--brand-red)" stroke-width="2"/>
      <circle cx="894" cy="486" r="7" fill="none" stroke="var(--accent-purple)" stroke-width="2"/>
      <circle cx="894" cy="486" r="2.5" fill="var(--accent-purple)"/>
    </g>
  </svg>

  <header class="header">
    <h1 class="header-title">OKAV drives is work through Global and Regional Partnerships</h1>
  </header>

  <section class="info-block frameworks">
    <h2 class="info-heading">Frameworks</h2>
    <ul class="info-list">
      <li>Social Accountability &amp;<br>Accreditation</li>
      <li>Interprofessional Education &amp;<br>Team-based Care</li>
      <li>Population Health</li>
    </ul>
  </section>

  <section class="info-block best-practices">
    <h2 class="info-heading">Network Knowledge<br>Best Practices</h2>
    <ul class="info-list">
      <li>Remote/Rural, Women, Migrants,<br>Refugees, Indigenous Health</li>
    </ul>
  </section>

  <section class="info-block guiding-values">
    <h2 class="info-heading">Guiding Values</h2>
    <ul class="info-list">
      <li>Community relevance</li>
      <li>Informed consumer</li>
      <li>Patient/Consumer voice</li>
      <li>Intersectoral, multi-disciplinary</li>
    </ul>
  </section>

  <section class="info-block outcome">
    <h2 class="info-heading">Outcome</h2>
    <ul class="info-list">
      <li>Coordinated Action by Local<br>Change Agents and Networks</li>
    </ul>
  </section>

  <div class="axis-label axis-global">Global Policy</div>
  <div class="axis-label axis-local">Local Action</div>

</main>
</body>
</html>
```